Whiskey Bottle Label

I am looking for an image to accompany a whiskey label. I am a Northbrook Pelicans fan and I am going to call my Whiskey Delphine's Red Anchor Whiskey and I need an image. Something that has a fighting cock / rooster theme.

My whiskey will not be for sale, but for gifts to my clients and friends.

```html
<!DOCTYPE html>
<html lang="en">
<head>
<meta charset="utf-8">
<title>Delphine's Red Anchor Whiskey – Label</title>
<link rel="stylesheet" href="https://fonts.googleapis.com/css2?family=Abril+Fatface&family=Playfair+Display:wght@700&family=Pinyon+Script&display=swap">
<style>
  :root {
    --page: #ffffff;
    --label: #d2cec1;
    --label-edge: #c4bfb0;
    --ink: #2f2e2c;
    --red: #9a3242;
    --grey: #9c9a94;
    --rooster-dark: #4a4846;
    --rooster-pink: #c9a3a3;
  }
  * { box-sizing: border-box; margin: 0; padding: 0; }
  html, body {
    width: 900px;
    height: 1200px;
    overflow: hidden;
    background: var(--page);
  }
  .canvas {
    position: relative;
    width: 900px;
    height: 1200px;
  }
  .label {
    position: absolute;
    left: 110px;
    top: 70px;
    width: 680px;
    height: 1060px;
    background: var(--label);
    box-shadow: inset 0 0 0 1px var(--label-edge);
    color: var(--ink);
  }
  .origin {
    position: absolute;
    right: 36px;
    top: 84px;
    font-family: "Pinyon Script", cursive;
    font-size: 27px;
    line-height: 1.1;
    text-align: right;
    color: var(--ink);
  }
  .origin span { display: block; }
  .origin .from { margin-right: 50px; }
  .origin .place { margin-top: 6px; }
  .rooster-art {
    position: absolute;
    left: 33px;
    top: 200px;
    width: 470px;
    height: 520px;
    background:
      radial-gradient(ellipse at 35% 30%, rgba(201,163,163,0.55), rgba(201,163,163,0) 60%),
      radial-gradient(ellipse at 55% 45%, rgba(74,72,70,0.45), rgba(74,72,70,0) 65%);
  }
  .title {
    position: absolute;
    right: 28px;
    top: 480px;
    text-align: right;
    font-family: "Abril Fatface", serif;
    line-height: 1;
  }
  .title .owner {
    display: block;
    font-size: 78px;
    color: var(--ink);
  }
  .title .name {
    display: block;
    font-size: 92px;
    color: var(--red);
    margin-top: 6px;
    white-space: nowrap;
  }
  .title .kind {
    display: block;
    font-size: 80px;
    color: var(--ink);
    margin-top: 18px;
    margin-right: 110px;
  }
  .spec {
    position: absolute;
    top: 930px;
    width: 130px;
    text-align: center;
  }
  .spec.volume { left: 70px; }
  .spec.strength { right: 42px; }
  .spec .value {
    display: block;
    font-family: "Pinyon Script", cursive;
    font-size: 28px;
    line-height: 1;
    padding-bottom: 6px;
    border-bottom: 2px dotted var(--ink);
  }
  .spec .unit {
    display: block;
    font-family: "Playfair Display", serif;
    font-weight: 700;
    font-size: 25px;
    margin-top: 8px;
    color: #6b6a66;
  }
  .house-mark {
    position: absolute;
    left: 250px;
    top: 930px;
    width: 200px;
    display: flex;
    align-items: center;
    justify-content: center;
    gap: 10px;
    font-family: "Abril Fatface", serif;
    font-size: 34px;
    color: var(--grey);
    height: 80px;
  }
  .house-mark .dot {
    width: 14px;
    height: 14px;
    border-radius: 50%;
    background: var(--grey);
  }
</style>
</head>
<body>
<main class="canvas">
  <section class="label">
    <p class="origin">
      <span class="from">from</span>
      <span>Delphine's family</span>
      <span class="place">Northbrook</span>
    </p>

    <div class="rooster-art" role="img" aria-label="Illustration of a fighting rooster leaping with wings spread and talons forward, in charcoal and dusty pink"></div>

    <h1 class="title">
      <span class="owner">Delphine's</span>
      <span class="name">Red Anchor</span>
      <span class="kind">Whiskey</span>
    </h1>

    <div class="spec volume">
      <span class="value">750 ml</span>
      <span class="unit">net.wt</span>
    </div>

    <div class="house-mark">
      <span class="dot"></span>
      <span>Delphine's</span>
    </div>

    <div class="spec strength">
      <span class="value">42%</span>
      <span class="unit">alc/vol</span>
    </div>
  </section>
</main>
</body>
</html>
```